Letterhead Design Project

Attached is our new Logo and a copy of our old letter head
Looking to rebrand with our new logo

Reason: I want to show a business card design

Industry/Entity Type

Film Production

Colors

Requirements
Must have
• The information on the old letterhead

```html
<!DOCTYPE html>
<html lang="en">
<head>
<meta charset="utf-8">
<title>Vantra International Letterhead</title>
<link href="https://fonts.googleapis.com/css2?family=Open+Sans:wght@400;600;700&display=swap" rel="stylesheet">
<style>
  :root {
    --backdrop: #9c9c9c;
    --paper: #ffffff;
    --paper-shade: #ebebeb;
    --brand-blue: #1a8dbf;
    --brand-blue-dark: #0f6f9c;
    --brand-orange: #e5731f;
    --ink: #2b2b2b;
    --white: #ffffff;
  }
  * { margin: 0; padding: 0; box-sizing: border-box; }
  html, body {
    width: 1079px; height: 1200px; overflow: hidden;
    background: var(--backdrop);
    font-family: "Open Sans", Arial, sans-serif;
  }
  .letterhead {
    position: absolute; left: 136px; top: 30px;
    width: 806px; height: 1140px;
    background: linear-gradient(180deg, var(--paper) 0%, var(--paper) 45%, var(--paper-shade) 100%);
    box-shadow: 0 6px 18px rgba(0,0,0,0.3);
    overflow: hidden;
  }
  .brand {
    position: absolute; left: 62px; top: 70px;
    display: flex; align-items: center; gap: 10px;
  }
  .brand-dot { width: 16px; height: 16px; border-radius: 50%; background: var(--brand-orange); }
  .brand-name {
    font-size: 30px; font-weight: 700; color: var(--brand-blue-dark);
    letter-spacing: 0.5px;
  }
  .contact {
    position: absolute; right: 62px; top: 74px;
    font-size: 11px; line-height: 16px; color: var(--ink);
  }
  .contact-line { display: flex; align-items: center; gap: 6px; }
  .contact-line svg { width: 10px; height: 10px; flex: none; }
  .contact-sep { margin: 0 4px; }
  .footer { position: absolute; left: 0; bottom: 0; width: 806px; height: 150px; }
  .footer svg { position: absolute; inset: 0; }
  .footer-web {
    position: absolute; right: 48px; top: 30px;
    font-size: 13px; font-weight: 600; letter-spacing: 3px; color: var(--white);
  }
  .footer-divisions {
    position: absolute; left: 30px; bottom: 36px;
    font-size: 14px; font-weight: 700; color: var(--white);
  }
  .footer-legal {
    position: absolute; left: 30px; bottom: 16px;
    font-size: 13px; color: var(--white);
  }
</style>
</head>
<body>
  <main class="letterhead">
    <header class="brand">
      <span class="brand-dot"></span>
      <span class="brand-name">Vantra International</span>
    </header>

    <address class="contact" style="font-style:normal">
      <div class="contact-line">
        <svg viewBox="0 0 10 10"><path d="M5 0a3.5 3.5 0 0 0-3.5 3.5C1.5 6 5 10 5 10s3.5-4 3.5-6.5A3.5 3.5 0 0 0 5 0z" fill="var(--brand-blue)"/><circle cx="5" cy="3.5" r="1.2" fill="#fff"/></svg>
        P.O. Box 418 Brookvale QLD 4306
      </div>
      <div class="contact-line">
        <svg viewBox="0 0 10 10"><path d="M5 0a3.5 3.5 0 0 0-3.5 3.5C1.5 6 5 10 5 10s3.5-4 3.5-6.5A3.5 3.5 0 0 0 5 0z" fill="var(--brand-blue)"/><circle cx="5" cy="3.5" r="1.2" fill="#fff"/></svg>
        P.O. Box 372 Marlow NSW 2172
      </div>
      <div class="contact-line">
        <svg viewBox="0 0 10 10"><path d="M2 0.5l2 2-1 1.5c.6 1.3 1.7 2.4 3 3l1.5-1 2 2-1.5 1.5C4.5 9.5.5 5.5 0.5 2z" fill="var(--brand-blue)"/></svg>
        0400 555 012
        <span class="contact-sep">|</span>
        <svg viewBox="0 0 10 10"><rect x="0.5" y="2" width="9" height="6.5" rx="1" fill="var(--brand-blue)"/><path d="M1 2.5l4 3 4-3" stroke="#fff" stroke-width="0.9" fill="none"/></svg>
        hello@vantra.com.au
      </div>
    </address>

    <footer class="footer">
      <svg viewBox="0 0 806 150" preserveAspectRatio="none" aria-hidden="true">
        <polygon points="500,20 806,20 806,44 520,44" fill="var(--brand-orange)"/>
        <polygon points="0,90 520,90 540,70 806,70 806,150 0,150" fill="var(--brand-blue)"/>
        <polygon points="520,44 806,44 806,56 532,56" fill="var(--white)"/>
        <polygon points="532,56 806,56 806,70 540,70 520,90 0,90 0,84 517,84" fill="var(--brand-blue)"/>
      </svg>
      <span class="footer-web">www.vantra.com.au</span>
      <p class="footer-divisions">Vantra Film Services | Vantra Pilot Escorts | Vantra Tour Management | Vantra Driver</p>
      <p class="footer-legal">are divisions of Vantra International Pty Ltd | ACN 104 582 376 &nbsp;ABN 48 104 582 376</p>
    </footer>
  </main>
</body>
</html>
```